Tea box package for Herbal Teas

We would like a design for a package of our tea products. We want the consumer to understand that our products are natural just by looking at the package. We prefer minimalistic designs.
The package we want would be a square (or slightly rectangular) box. The box would be generic enough for us to use it for different teas. Essentially what we want is all the main information and designs to be the same for each tea product we have. We would like to be able to change the main color and the name of the tea then to customize to the tea in the package. Please see the attached images for examples.
We really like the package in tea_packaging_example_4 picture. We would like our packaging to be something very similar but with all the labels printed on the package.
We already have our logo so I am attaching that as well (image named 'velka brin logo copy'). That would go on the front of the box.
We also attach a tile created using our logo (see image called 'tile'). We would like this to go to the sides similarly to tea_packaging_example_4.
On the back of the pouch, we want to have directions on how to make the tea but we want this section to be editable. For now just 3-4 lines of sample text is fine along with instructions on how to make a tea, see picture 'back of tea box'.
We would like for the box color to be as in example picture
tea_packaging_example_4. The color of the writing should be the same as the logo color. The font style should be something that would look nice next to the logo font, we are not sure what that font should be. The only thing colored would be the name of the tea and the ribbon as seen in tea_packaging_example_4, which we would like to change if we need to, to other variations.
Thanks a lot. For any questions, please contact me.

```html
<!DOCTYPE html>
<html lang="en">
<head>
<meta charset="utf-8">
<title>Ceylon Black Tea – Box Panels</title>
<link href="https://fonts.googleapis.com/css2?family=Questrial&family=Barlow:wght@400;600&display=swap" rel="stylesheet">
<style>
  :root {
    --kraft: #cfb08a;
    --kraft-deep: #c2a27c;
    --ink: #383838;
    --ribbon: #ee7d1a;
    --gold-a: #b8913a;
    --gold-b: #f3dc8c;
    --paper: #ffffff;
  }
  * { box-sizing: border-box; margin: 0; padding: 0; }
  html, body { width: 1000px; height: 1200px; overflow: hidden; background: var(--paper); }
  .sheet {
    position: absolute; left: 73px; top: 173px;
    display: grid; grid-template-columns: 420px 420px; grid-template-rows: 420px 420px; gap: 14px;
  }
  .panel { position: relative; width: 420px; height: 420px; background: var(--kraft); overflow: hidden; }

  .tile-pattern {
    position: absolute; left: 40px; top: 40px; width: 340px; height: 340px;
    background: linear-gradient(135deg, #8f7c63 0%, #a48d70 50%, #8f7c63 100%);
    opacity: .75;
  }
  .faint-ornament {
    position: absolute; left: 43px; top: 86px; width: 335px; height: 272px;
    background: var(--kraft-deep); border-radius: 45%;
  }
  .ribbon-straight {
    position: absolute; left: 132px; top: 0; width: 156px; height: 420px;
    background: linear-gradient(90deg, var(--gold-a), var(--gold-b) 50%, var(--gold-a));
    padding: 0 6px;
  }
  .ribbon-straight .ribbon-fill {
    width: 100%; height: 100%; background: var(--ribbon);
    display: flex; flex-direction: column; align-items: center; justify-content: center; gap: 26px;
  }
  .flipped { transform: rotate(180deg); }
  .tea-name {
    font-family: "Questrial", sans-serif; color: var(--paper); text-align: center;
    line-height: 1; letter-spacing: 2px; font-weight: 700;
  }
  .tea-name.dark { color: var(--ink); }
  .tea-name .main { display: block; font-size: 25px; }
  .tea-name .sub { display: block; font-size: 15px; letter-spacing: 1.5px; margin-top: 2px; }
  .brand-disc {
    width: 106px; height: 106px; border-radius: 50%; background: var(--paper);
    display: flex; align-items: center; justify-content: center;
  }
  .brand-name {
    font-family: "Questrial", sans-serif; font-size: 12px; color: var(--ink); letter-spacing: 1px;
    text-transform: uppercase;
  }

  .info-card {
    position: absolute; left: 52px; top: 55px; width: 313px; height: 309px;
    background: var(--ink); color: var(--paper);
    font-family: "Barlow", sans-serif;
  }
  .label-tab { position: absolute; left: 130px; top: 0; width: 160px; height: 89px; }
  .label-tab svg { position: absolute; inset: 0; }
  .label-tab .tea-name { position: absolute; left: 0; right: 0; top: 28px; }
  .label-tab .main { font-size: 19px; }
  .label-tab .sub { font-size: 12px; }
  .about { position: absolute; left: 22px; top: 59px; width: 272px; }
  .about h2 { font-size: 10px; font-weight: 600; margin-bottom: 2px; }
  .about p { font-size: 9.5px; line-height: 1.2; }
  .method { position: absolute; left: 22px; top: 174px; }
  .method h2 { font-size: 10px; font-weight: 600; margin-bottom: 4px; }
  .steps { display: flex; gap: 16px; }
  .step {
    width: 47px; height: 47px; border: 1.5px solid var(--paper); border-radius: 8px;
    display: flex; flex-direction: column; align-items: center; justify-content: center;
    font-size: 6px; line-height: 1.1; text-align: center; font-weight: 600;
  }
  .step svg { width: 18px; height: 18px; margin-bottom: 2px; }

  .front-ornament {
    position: absolute; left: 40px; top: 76px; width: 338px; height: 306px;
    background: var(--ink); border-radius: 44%;
  }
  .ribbon-point { position: absolute; left: 132px; top: 0; width: 156px; height: 272px; }
  .ribbon-point svg { position: absolute; inset: 0; }
  .ribbon-point .brand-disc { position: absolute; left: 25px; top: 40px; }
  .ribbon-point .tea-name { position: absolute; left: 0; right: 0; top: 176px; }
</style>
</head>
<body>
<main class="sheet">
  <section class="panel side-panel">
    <div class="tile-pattern" role="img" aria-label="Repeating grid of ornamental tiles in dark ink on kraft"></div>
  </section>

  <section class="panel top-panel">
    <div class="faint-ornament" role="img" aria-label="Faint tonal ornament on kraft"></div>
    <div class="ribbon-straight">
      <div class="ribbon-fill flipped">
        <div class="brand-disc"><span class="brand-name">Velka Brin</span></div>
        <div class="tea-name dark"><span class="main">CEYLON</span><span class="sub">BLACK TEA</span></div>
      </div>
    </div>
  </section>

  <section class="panel back-panel">
    <div class="info-card">
      <div class="about">
        <h2>What's special about this tea?</h2>
        <p>Grown in the Fujian proince of China, tea buds are plucked within two hours of sprouting, then withered naturally in the sun. If your usual white tea appears green in your cup, then it is green tea, this, however, is the genuine article. Possibly one of our most exclusive teas - refreshing, light and aromatic.</p>
      </div>
      <div class="method">
        <h2>How we like it:</h2>
        <div class="steps">
          <div class="step">
            <svg viewBox="0 0 20 20" fill="none" stroke="#fff" stroke-width="1.5"><rect x="5" y="8" width="10" height="9" rx="1"/><path d="M10 8V3h4"/></svg>
            tea<br>1 per person
          </div>
          <div class="step">
            <svg viewBox="0 0 20 20" fill="none" stroke="#fff" stroke-width="1.5"><path d="M3 9h14a7 7 0 0 1-14 0z"/><path d="M8 3c0 2 2 2 2 4M12 3c0 2 2 2 2 4"/></svg>
            water<br>80°C
          </div>
          <div class="step">
            <svg viewBox="0 0 20 20" fill="none" stroke="#fff" stroke-width="1.5"><circle cx="6" cy="6" r="4"/><path d="M6 4v2h2"/><path d="M8 11h9v3a4 4 0 0 1-4 4h-1a4 4 0 0 1-4-4z"/></svg>
            brew<br>3-5 minutes
          </div>
        </div>
      </div>
    </div>
    <div class="label-tab">
      <svg width="160" height="89" viewBox="0 0 160 89">
        <defs><linearGradient id="goldBack" x1="0" x2="1"><stop offset="0" stop-color="#b8913a"/><stop offset=".5" stop-color="#f3dc8c"/><stop offset="1" stop-color="#b8913a"/></linearGradient></defs>
        <rect width="160" height="89" fill="url(#goldBack)"/>
        <rect x="6" y="0" width="148" height="83" fill="#ee7d1a"/>
      </svg>
      <div class="tea-name"><span class="main">CEYLON</span><span class="sub">BLACK TEA</span></div>
    </div>
  </section>

  <section class="panel front-panel">
    <div class="front-ornament" role="img" aria-label="Large dark ornamental medallion behind the ribbon"></div>
    <div class="ribbon-point">
      <svg width="156" height="272" viewBox="0 0 156 272">
        <defs><linearGradient id="goldFront" x1="0" x2="1"><stop offset="0" stop-color="#b8913a"/><stop offset=".5" stop-color="#f3dc8c"/><stop offset="1" stop-color="#b8913a"/></linearGradient></defs>
        <polygon points="0,0 156,0 156,245 78,272 0,245" fill="url(#goldFront)"/>
        <polygon points="6,0 150,0 150,240 78,265 6,240" fill="#ee7d1a"/>
      </svg>
      <div class="brand-disc"><span class="brand-name">Velka Brin</span></div>
      <div class="tea-name"><span class="main">CEYLON</span><span class="sub">BLACK TEA</span></div>
    </div>
  </section>
</main>
</body>
</html>
```